Business Card for a Wedding Films Business

We require a business card design for our business 'Lewis Marrow Wedding Films'. The logo needs to look classy and high end.

Target Market(s)

Wedding Couples

Contact Information for Business Card

Lewis Marrow Wedding Films
07312 605 227
films@lewismarrowreels.com
www.lewismarrowreels.com

Facebook: @lewismarrowweddingfilms
Instagram: @lewismarrowfilms

Font styles to use
Sans Serif

Requirements
Must have
• Social media icons - Facebook and Instagram

```html
<!DOCTYPE html>
<html lang="en">
<head>
<meta charset="utf-8">
<title>Lewis Marrow Wedding Films – Business Card</title>
<link rel="stylesheet" href="https://fonts.googleapis.com/css2?family=Montserrat:wght@400;500&display=swap">
<style>
  :root {
    --backdrop: #3a3b3d;
    --card-dark: #2b2b2c;
    --card-light: #ffffff;
    --silver: #c9cacc;
    --ink: #1c1c1c;
    --muted: #555a5e;
    --rule: #9a9a9a;
    --social-fb: #2f4f9a;
    --social-ig: #d8436f;
  }
  * { margin: 0; padding: 0; box-sizing: border-box; }
  html, body {
    width: 1200px; height: 1000px; overflow: hidden;
    background: var(--backdrop);
    font-family: "Montserrat", sans-serif;
  }
  .stage { position: relative; width: 1200px; height: 1000px; }

  .card {
    position: absolute;
    width: 560px; height: 320px;
    border-radius: 26px;
    display: flex; flex-direction: column; align-items: center; justify-content: center;
  }
  .card--back { left: 110px; top: 110px; background: var(--card-dark); }
  .card--front { left: 530px; top: 540px; background: var(--card-light); }

  .wordmark {
    display: flex; flex-direction: column; align-items: center;
    font-weight: 500; text-transform: uppercase; text-align: center;
  }
  .wordmark__mark {
    width: 14px; height: 14px; margin-bottom: 14px;
  }
  .wordmark__name { font-size: 30px; letter-spacing: 0.22em; line-height: 1.1; }
  .wordmark__tag { font-size: 13px; letter-spacing: 0.55em; margin-top: 6px; }

  .card--back .wordmark { color: var(--silver); }
  .card--back .wordmark__mark { background: var(--silver); }
  .card--front .wordmark { color: var(--ink); }
  .card--front .wordmark__mark { background: var(--ink); }
  .card--front .wordmark__name { font-size: 26px; }
  .card--front .wordmark__tag { font-size: 11px; }

  .divider {
    width: 70px; height: 2px; margin: 14px 0 18px;
    background: linear-gradient(90deg, transparent, var(--rule), transparent);
  }

  .contacts { display: flex; flex-direction: column; align-items: center; gap: 8px; }
  .contacts__row {
    display: flex; align-items: center; gap: 7px;
    font-size: 10.5px; font-weight: 400; color: var(--muted); white-space: nowrap;
  }
  .contacts__row strong { font-weight: 500; color: var(--ink); }
  .contacts__sep { width: 4px; height: 4px; border-radius: 50%; background: var(--muted); }
  .icon { width: 12px; height: 12px; flex: none; }
  .social-dot { width: 11px; height: 11px; border-radius: 50%; flex: none; }
  .social-dot--fb { background: var(--social-fb); }
  .social-dot--ig { background: var(--social-ig); }
</style>
</head>
<body>
<main class="stage">

  <section class="card card--back" aria-label="Card back">
    <div class="wordmark">
      <span class="wordmark__mark"></span>
      <span class="wordmark__name">Lewis Marrow</span>
      <span class="wordmark__tag">Wedding Films</span>
    </div>
  </section>

  <section class="card card--front" aria-label="Card front">
    <div class="wordmark">
      <span class="wordmark__mark"></span>
      <span class="wordmark__name">Lewis Marrow</span>
      <span class="wordmark__tag">Wedding Films</span>
    </div>
    <div class="divider"></div>
    <div class="contacts">
      <div class="contacts__row">
        <svg class="icon" viewBox="0 0 24 24" aria-hidden="true"><path d="M6.6 2.5l3 3.2-1.8 2.6c1.3 2.8 3.4 4.9 6.2 6.2l2.6-1.8 3.2 3-1.6 3.2C10.6 19 5 13.4 3.4 4.1z" fill="#7b7f83"/></svg>
        <span>07312 605 227</span>
        <span class="contacts__sep"></span>
        <svg class="icon" viewBox="0 0 24 24" aria-hidden="true"><rect x="2" y="5" width="20" height="14" fill="#7b7f83"/><path d="M2 5l10 8 10-8" fill="none" stroke="#fff" stroke-width="1.6"/></svg>
        <span>films@<strong>lewismarrowreels</strong>.com</span>
        <span class="contacts__sep"></span>
        <svg class="icon" viewBox="0 0 24 24" aria-hidden="true"><g fill="none" stroke="#7b7f83" stroke-width="1.6"><circle cx="12" cy="12" r="10"/><ellipse cx="12" cy="12" rx="4.5" ry="10"/><path d="M2 12h20M4 7h16M4 17h16"/></g></svg>
        <span>www.<strong>lewismarrowreels</strong>.com</span>
      </div>
      <div class="contacts__row">
        <span class="social-dot social-dot--fb"></span>
        <strong>@lewismarrowweddingfilms</strong>
        <span style="width:10px"></span>
        <span class="social-dot social-dot--ig"></span>
        <strong>@lewismarrowfilms</strong>
      </div>
    </div>
  </section>

</main>
</body>
</html>
```